BRIGHTDOOR7 - business card, letterhead and envelopes
BRIGHTDOOR7 - Business cards, letterhead and envelopes
Professional
BRIGHTDOOR7 LLC
Real Estate Solution Provider
info@brightdoor7.example
www.brightdoor7.example
We specialize in creative real estate solutions
We pay cash for houses!
We prevent foreclosures !
We help repair credit!
We pay referral fees!

```html
<!DOCTYPE html>
<html lang="en">
<head>
<meta charset="utf-8">
<title>BRIGHTDOOR7 – Stationery Set</title>
<link rel="stylesheet" href="https://fonts.googleapis.com/css2?family=Open+Sans:wght@400;600&display=swap">
<style>
  :root {
    --bg: #dcdcdc;
    --paper: #ffffff;
    --ink: #0d0d0d;
    --gold: #c9a24a;
    --light: #f2f2f2;
    --blue: #2f5fb3;
    --line: #cfcfcf;
  }
  * { box-sizing: border-box; margin: 0; padding: 0; }
  html, body { width: 1200px; height: 910px; overflow: hidden; }
  body { background: var(--bg); font-family: "Open Sans", Arial, sans-serif; position: relative; }

  .sheet { position: absolute; background: var(--paper); box-shadow: 0 6px 18px rgba(0,0,0,.18); overflow: hidden; }

  /* name block */
  .brand-block { background: var(--ink); display: flex; align-items: center; justify-content: center; }
  .brand-name { font-family: "Open Sans", Arial, sans-serif; font-weight: 600; color: var(--light); letter-spacing: .04em; display: flex; align-items: center; gap: 8px; white-space: nowrap; }
  .brand-dot { width: .5em; height: .5em; border-radius: 50%; background: var(--blue); display: inline-block; }

  .contact-list { list-style: none; color: var(--gold); }
  .contact-list li { display: flex; align-items: center; gap: 7px; line-height: 1.6; white-space: nowrap; }
  .contact-list .dot { width: 7px; height: 7px; border-radius: 50%; background: var(--blue); flex: none; }

  /* letterhead */
  .letterhead { left: 50px; top: 67px; width: 600px; height: 776px; }
  .letterhead .brand-block { position: absolute; left: 30px; top: 32px; width: 250px; height: 110px; border-radius: 10px 10px 28px 10px; }
  .letterhead .brand-name { font-size: 24px; }
  .letterhead .contact-list { position: absolute; left: 298px; top: 36px; font-size: 11px; }
  .letterhead .footer-band { position: absolute; left: 40px; right: 40px; bottom: 0; height: 28px; background: var(--ink); border-radius: 16px 16px 0 0; }

  /* envelope */
  .envelope { left: 700px; top: 80px; width: 450px; height: 196px; }
  .envelope .flap-band { position: absolute; left: 0; right: 0; top: 0; height: 40px; background: var(--ink); }
  .envelope .postage { position: absolute; right: 16px; top: 13px; font-weight: 600; font-size: 10px; color: var(--paper); letter-spacing: .1em; }
  .envelope .brand-block { position: absolute; left: 18px; top: 40px; width: 160px; height: 66px; border-radius: 0 0 18px 8px; }
  .envelope .brand-name { font-size: 15px; gap: 6px; }
  .envelope .contact-list { position: absolute; left: 192px; top: 48px; font-size: 8px; }
  .envelope .address-window { position: absolute; left: 22px; bottom: 26px; width: 170px; height: 46px; border: 1px solid var(--line); border-radius: 6px; }
  .envelope .footer-band { position: absolute; left: 0; right: 0; bottom: 0; height: 12px; background: var(--ink); }

  /* business cards */
  .card { width: 350px; height: 200px; border-radius: 12px; }
  .card-front { left: 750px; top: 330px; }
  .card-front .brand-block { position: absolute; left: 75px; top: 16px; width: 200px; height: 76px; border-radius: 10px; }
  .card-front .brand-name { font-size: 18px; }
  .card-front .contact-list { position: absolute; left: 90px; top: 106px; font-size: 9px; }

  .card-back { left: 750px; top: 580px; background: var(--ink); }
  .card-back .brand-block { position: absolute; left: 0; right: 0; top: 30px; height: 40px; }
  .card-back .brand-name { font-size: 21px; }
  .card-back .promises { position: absolute; left: 0; right: 0; top: 100px; text-align: center; color: var(--gold); font-size: 9px; line-height: 1.55; list-style: none; }
  .card-back .promises .lead { font-weight: 600; }
</style>
</head>
<body>

<section class="sheet letterhead" aria-label="Letterhead">
  <div class="brand-block">
    <div class="brand-name"><span class="brand-dot"></span>BRIGHTDOOR7</div>
  </div>
  <ul class="contact-list">
    <li><span class="dot"></span>(555) 014-2290</li>
    <li><span class="dot"></span>1480 Harbor Lane, Fairview, MD</li>
    <li><span class="dot"></span>(555) 014-2291</li>
    <li><span class="dot"></span>info@brightdoor7.example</li>
    <li><span class="dot"></span>www.brightdoor7.example</li>
  </ul>
  <div class="footer-band"></div>
</section>

<section class="sheet envelope" aria-label="Envelope">
  <div class="flap-band"></div>
  <div class="postage">FIRST CLASS</div>
  <div class="brand-block">
    <div class="brand-name"><span class="brand-dot"></span>BRIGHTDOOR7</div>
  </div>
  <ul class="contact-list">
    <li><span class="dot"></span>(555) 014-2290</li>
    <li><span class="dot"></span>1480 Harbor Lane, Fairview, MD</li>
    <li><span class="dot"></span>(555) 014-2291</li>
    <li><span class="dot"></span>info@brightdoor7.example</li>
    <li><span class="dot"></span>www.brightdoor7.example</li>
  </ul>
  <div class="address-window"></div>
  <div class="footer-band"></div>
</section>

<section class="sheet card card-front" aria-label="Business card front">
  <div class="brand-block">
    <div class="brand-name"><span class="brand-dot"></span>BRIGHTDOOR7</div>
  </div>
  <ul class="contact-list">
    <li><span class="dot"></span>(555) 014-2290</li>
    <li><span class="dot"></span>1480 Harbor Lane, Fairview, MD</li>
    <li><span class="dot"></span>(555) 014-2291</li>
    <li><span class="dot"></span>info@brightdoor7.example</li>
  </ul>
</section>

<section class="sheet card card-back" aria-label="Business card back">
  <div class="brand-block">
    <div class="brand-name"><span class="brand-dot"></span>BRIGHTDOOR7</div>
  </div>
  <ul class="promises">
    <li class="lead">We specialize in creative real estate solutions</li>
    <li>We pay cash for houses!</li>
    <li>We prevent foreclosures!</li>
    <li>We help repair credit!</li>
  </ul>
</section>

</body>
</html>
```